Quellbrook Supply Chain and Logistic Consulting

Please review the attached Business Card. I want as close to this card with the colors, fonts, and quality of the card as possible. The attached compass should replace the deer head on both sides of the card and the text should say:

Backside
Compass JPEG
Quellbrook Partners
A Supply Chain and Logistics Consulting Company

Frontside
Quellbrook Partners
Ross Pelgrave - Harlow Bay
President
____________________________________
(555) 214-9037
QuellbrookSCL@Mailvento.com
_____________________________________

Bottom Front Side

Target Market(s)

Businesses

Contact Information for Business Card

Backside
Compass JPEG
Quellbrook Partners

Frontside
Quellbrook Partners
President
(555) 214-9037
QuellbrookSCL@Mailvento.com

Bottom Front Side

Font styles to use
Serif
Script

Colors

Designer to choose colors to be used in the design.

Requirements
Must have
• See attached card for reference
Nice to have
Should not have

```html
<!DOCTYPE html>
<html lang="en">
<head>
<meta charset="utf-8">
<title>Quellbrook Partners — Business Card</title>
<link rel="stylesheet" href="https://fonts.googleapis.com/css2?family=Cinzel:wght@400;500&family=Tinos:wght@400&display=swap">
<style>
  :root {
    --page: #2b2b2e;
    --card: #1c1d1f;
    --card-edge: #26272a;
    --ink: #f2f2f2;
    --ink-soft: #cfd0d2;
    --rule: #bfc0c2;
    --ghost: #232427;
  }
  * { box-sizing: border-box; margin: 0; padding: 0; }
  html, body { width: 1200px; height: 800px; overflow: hidden; background: var(--page); }
  .canvas { position: relative; width: 1200px; height: 800px; }

  .card {
    position: absolute;
    top: 246px;
    width: 540px;
    height: 308px;
    border-radius: 18px;
    background: var(--card);
    border: 1px solid var(--card-edge);
    overflow: hidden;
    color: var(--ink);
    font-family: "Tinos", "Times New Roman", serif;
  }
  .card--brand { left: 40px; }
  .card--contact { left: 620px; }

  /* Brand side */
  .brand-mark {
    position: absolute;
    top: 50px; left: 0; right: 0;
    display: flex; align-items: center; justify-content: center; gap: 12px;
  }
  .brand-mark__dot { width: 36px; height: 36px; border-radius: 50%; border: 2px solid var(--ink-soft); }
  .brand-mark__name { font-size: 28px; color: var(--ink-soft); letter-spacing: 1px; }

  .brand-title {
    position: absolute; top: 178px; left: 0; right: 0;
    text-align: center;
    font-family: "Cinzel", "Times New Roman", serif;
    font-weight: 400;
    font-size: 32px; letter-spacing: 1.5px;
    white-space: nowrap;
  }
  .brand-tagline {
    position: absolute; top: 226px; left: 0; right: 0;
    text-align: center; font-size: 13px; letter-spacing: 0.8px; text-transform: uppercase;
    color: var(--ink-soft);
  }

  /* Contact side */
  .contact-ghost {
    position: absolute; top: -70px; right: -60px;
    width: 240px; height: 240px; border-radius: 50%;
    background: var(--ghost);
  }
  .contact-block { position: absolute; top: 40px; left: 36px; width: 310px; text-align: center; }
  .contact-title {
    font-family: "Cinzel", "Times New Roman", serif; font-weight: 400;
    font-size: 24px; letter-spacing: 1px; white-space: nowrap;
  }
  .contact-tagline { font-size: 9.5px; letter-spacing: 0.5px; text-transform: uppercase; color: var(--ink-soft); margin-top: 4px; white-space: nowrap; }
  .contact-name { font-size: 19px; margin-top: 14px; }
  .contact-role { font-size: 13px; color: var(--ink-soft); }
  .contact-rule { height: 1px; background: var(--rule); margin: 8px 34px; }
  .contact-line { font-size: 14px; line-height: 1.45; }

  .footer-band {
    position: absolute; left: 30px; right: 30px; bottom: 30px;
    display: flex; align-items: center; gap: 12px;
  }
  .footer-band__rule { flex: 1; height: 1px; background: var(--rule); }
  .footer-band__text { font-size: 10px; letter-spacing: 0.6px; text-transform: uppercase; color: var(--ink-soft); white-space: nowrap; }
</style>
</head>
<body>
<main class="canvas">

  <section class="card card--brand" aria-label="Card back">
    <div class="brand-mark">
      <span class="brand-mark__dot"></span>
      <span class="brand-mark__name">Quellbrook</span>
    </div>
    <h1 class="brand-title">QUELLBROOK PARTNERS</h1>
    <p class="brand-tagline">A Supply Chain and Logistics Consulting Company</p>
  </section>

  <section class="card card--contact" aria-label="Card front">
    <div class="contact-ghost" aria-hidden="true"></div>
    <div class="contact-block">
      <h2 class="contact-title">QUELLBROOK PARTNERS</h2>
      <p class="contact-tagline">A Supply Chain and Logistics Consulting Company</p>
      <p class="contact-name">Ross Pelgrave &bull; Harlow Bay</p>
      <p class="contact-role">President</p>
      <div class="contact-rule"></div>
      <p class="contact-line">(555) 214-9037</p>
      <p class="contact-line">QuellbrookSCL@Mailvento.com</p>
      <div class="contact-rule"></div>
    </div>
    <div class="footer-band">
      <span class="footer-band__rule"></span>
      <span class="footer-band__text">A Supply Chain and Logistics Consulting Company</span>
      <span class="footer-band__rule"></span>
    </div>
  </section>

</main>
</body>
</html>
```